Birch Lane Electical winter special

I need an ad for a print magazine for my electrical contracting business.
It must have my logo and business name as the main back ground with a banner over the top stating 'winter solar special 10% off'
it must have my licence number in the botomm right corner lic.528194K
It must have my name Derek Malloway ph 0491823576
Also I would like it to say somewher 'Call now for your free solar assessment'
I would like it on a sharp black bagground like my business card attached and flyer attached
This will be a in a landscape design not potrait
Target Market(s)
Print ad and banner advertising
Industry/Entity Type
Solar Energy
Colors
Designer to choose colors to be used in the design.
Requirements
Must have
- my licence number on bottom right corner
- lic.528194K

```html
<!DOCTYPE html>
<html lang="en">
<head>
<meta charset="utf-8">
<title>Birch Lane Electical – Winter Solar Special</title>
<link rel="stylesheet" href="https://fonts.googleapis.com/css2?family=Barlow:wght@500;700;800&family=Barlow+Semi+Condensed:wght@500;600&family=Orbitron:wght@800&display=swap">
<style>
  :root{
    --ink:#000000;
    --page:#ffffff;
    --navy:#213f93;
    --sky:#27a9e1;
    --silver-top:#e9eaec;
    --silver-bottom:#a7a9ac;
    --ring:#e4e6ea;
    --text-dark:#1a1a1a;
    --text-muted:#555b61;
    --white:#ffffff;
  }
  html,body{margin:0;padding:0;width:987px;height:1200px;overflow:hidden;background:var(--page);}
  .canvas{position:relative;width:987px;height:1200px;}
  .ad{position:absolute;left:41px;top:48px;width:905px;height:452px;display:block;}
  .brand-name{font-family:"Barlow",sans-serif;font-weight:700;fill:var(--sky);}
  .call-line{font-family:"Barlow Semi Condensed",sans-serif;font-weight:600;fill:var(--white);}
  .free{font-family:"Barlow",sans-serif;font-weight:800;fill:var(--sky);}
  .assessment{font-family:"Barlow",sans-serif;font-weight:800;fill:var(--white);}
  .phone-number{font-family:"Orbitron",sans-serif;font-weight:800;fill:var(--text-dark);}
  .web{font-family:"Barlow",sans-serif;font-weight:700;fill:var(--text-dark);}
  .email{font-family:"Barlow",sans-serif;font-weight:500;fill:var(--text-dark);}
  .licence{font-family:"Barlow",sans-serif;font-weight:500;fill:var(--text-muted);}
  .badge-arc{font-family:"Barlow",sans-serif;font-weight:800;fill:var(--navy);}
  .badge-offer{font-family:"Barlow",sans-serif;font-weight:800;fill:var(--white);}
</style>
</head>
<body>
<div class="canvas">
<svg class="ad" viewBox="0 0 905 452" xmlns="http://www.w3.org/2000/svg">
  <defs>
    <linearGradient id="silverBand" x1="0" y1="0" x2="0" y2="1">
      <stop offset="0" stop-color="var(--silver-top)"/>
      <stop offset="1" stop-color="var(--silver-bottom)"/>
    </linearGradient>
    <linearGradient id="snowDrift" x1="0" y1="0" x2="1" y2="1">
      <stop offset="0" stop-color="var(--white)"/>
      <stop offset="1" stop-color="#cfe3ee"/>
    </linearGradient>
    <path id="arcTop" d="M 620 212 A 94 94 0 0 1 808 212"/>
    <path id="arcBottom" d="M 594 212 A 120 120 0 0 0 834 212"/>
  </defs>

  <rect class="backdrop" width="905" height="452" fill="var(--ink)"/>

  <path class="lower-band" d="M0 307 C 120 345 260 360 420 335 C 520 320 600 300 700 270 L 905 230 L 905 452 L 0 452 Z" fill="url(#silverBand)"/>
  <path class="band-edge" d="M0 307 C 120 345 260 360 420 335 C 520 320 600 300 700 270" fill="none" stroke="var(--navy)" stroke-width="7"/>

  <path class="snow" d="M820 250 C 850 225 880 220 905 228 L 905 310 C 880 295 850 288 820 288 Z" fill="url(#snowDrift)"/>
  <circle class="snowflake-area" role="img" aria-label="faint snowflake decoration" cx="721" cy="407" r="34" fill="var(--white)" opacity="0.3"/>

  <circle class="brand-dot" cx="226" cy="82" r="46" fill="var(--navy)"/>
  <text class="brand-name" x="226" y="192" font-size="46" text-anchor="middle" textLength="350" lengthAdjust="spacingAndGlyphs">BIRCH LANE</text>
  <text class="brand-name" x="226" y="218" font-size="19" text-anchor="middle" textLength="236" lengthAdjust="spacing">ELECTICAL</text>

  <text class="call-line" x="226" y="255" font-size="24" text-anchor="middle" textLength="235" lengthAdjust="spacingAndGlyphs">CALL NOW FOR YOUR</text>
  <text class="free" x="226" y="322" font-size="80" text-anchor="middle" textLength="269" lengthAdjust="spacingAndGlyphs">FREE</text>
  <text class="assessment" x="226" y="347" font-size="20" text-anchor="middle" textLength="224" lengthAdjust="spacingAndGlyphs">SOLAR ASSESSMENT</text>

  <g class="phone-icon" fill="var(--text-dark)">
    <path d="M28 402 C 28 392 40 388 59 388 C 78 388 90 392 90 402 L 90 408 L 76 408 L 76 400 L 42 400 L 42 408 L 28 408 Z"/>
    <path d="M38 412 L 80 412 L 86 436 L 32 436 Z"/>
    <g fill="var(--silver-top)">
      <rect x="50" y="416" width="5" height="4"/><rect x="57" y="416" width="5" height="4"/><rect x="64" y="416" width="5" height="4"/>
      <rect x="50" y="423" width="5" height="4"/><rect x="57" y="423" width="5" height="4"/><rect x="64" y="423" width="5" height="4"/>
      <rect x="50" y="430" width="5" height="3"/><rect x="57" y="430" width="5" height="3"/><rect x="64" y="430" width="5" height="3"/>
    </g>
  </g>
  <text class="phone-number" x="97" y="414" font-size="25" textLength="261" lengthAdjust="spacingAndGlyphs">0491823576</text>
  <text class="web" x="97" y="437" font-size="16" textLength="260" lengthAdjust="spacingAndGlyphs">www.birchlaneelectrical.com</text>
  <text class="email" x="367" y="437" font-size="16" textLength="289" lengthAdjust="spacingAndGlyphs">|&#160;&#160;info@birchlaneelectrical.com.au</text>
  <text class="licence" x="871" y="436" font-size="13" text-anchor="end">lic.528194K</text>

  <g class="badge">
    <circle cx="714" cy="212" r="140" fill="var(--navy)"/>
    <circle cx="714" cy="212" r="129" fill="var(--ring)"/>
    <circle cx="714" cy="212" r="86" fill="var(--navy)"/>
    <circle cx="714" cy="212" r="80" fill="var(--sky)"/>
    <text class="badge-arc" font-size="34" letter-spacing="1"><textPath href="#arcTop" startOffset="50%" text-anchor="middle">WINTER SOLAR</textPath></text>
    <text class="badge-arc" font-size="40" letter-spacing="3"><textPath href="#arcBottom" startOffset="50%" text-anchor="middle">SPECIAL</textPath></text>
    <g fill="var(--navy)">
      <polygon points="606,206 609,214 617,214 611,219 613,227 606,222 599,227 601,219 595,214 603,214"/>
      <polygon points="822,206 825,214 833,214 827,219 829,227 822,222 815,227 817,219 811,214 819,214"/>
    </g>
    <text class="badge-offer" x="714" y="203" font-size="56" text-anchor="middle">10%</text>
    <text class="badge-offer" x="714" y="258" font-size="56" text-anchor="middle">OFF</text>
  </g>
</svg>
</div>
</body>
</html>
```